WordPress Website Design - Harlow Auction

Need a WordPress design for an auction company wanting a responsive, simple and easy to use site. Current site to be upgraded: http://www.harlowbidhouse.example/

A site the client mentions liking is http://www.pendrakegavel.example. The attached logo color can be changed to suit your design - a different red, or green perhaps.

Industry/Entity Type

It Company

Number of Pages Required

1 page

Font styles to use
Serif
Sans Serif

Requirements
Must have
• Keep in mind this site will be built on a responsive theme.
• Site navigation: 1) Home, 2) Auctions, 3) Real Estate Listings, 4) Services, 5) Appraisals, 6) The Bidding Hall, 7) About Us, 8) Contact Us
• Site will have large, prominent full width (960px) slideshow - please pick one of the 3 attached images. Colors can be different than current site - wants a brighter site, colors complementing the logo. Home page will have auction list (the look of the auction list can be seen at http://www.bluefernlots.example/auction-calendar/)
• The widgets in the sidebar/header are: Email signup form, social media(FB Twitter, Youtube), News & Events blog, Testimonials, Featured Auctions, Featured Listings widget.
• Footer will have smaller company logo(below), contact info, and attached association logos.
• Dorian Harlow Auction-Realty
• 3418 Thistle Lane • New Harmony, IN 47209
• marcus@harlowbidhouse.example
• 812.555.0143
• 877.555.0178
Nice to have
• Design of dropdown menus: under Auctions, 1) Current Auctions, 2) Online Auctions, 3) Past Auctions

```html
<!DOCTYPE html>
<html lang="en">
<head>
<meta charset="utf-8">
<title>Harlow Auction</title>
<link href="https://fonts.googleapis.com/css2?family=Open+Sans:wght@400;600;700&family=Raleway:wght@500;700;800&display=swap" rel="stylesheet">
<style>
:root{
  --red:#e2333f;
  --ink:#222326;
  --nav:#2a2b2e;
  --text:#555a60;
  --muted:#8a8f95;
  --line:#e3e5e8;
  --page:#f1f2f4;
  --white:#ffffff;
  --footer:#1c1d20;
}
*{box-sizing:border-box;margin:0;padding:0}
html,body{width:1200px;height:3116px;overflow:hidden}
body{background:var(--page);font-family:"Open Sans",Arial,sans-serif;color:var(--text);font-size:12px;line-height:1.45}
.site-header{height:88px;background:var(--white);display:flex;align-items:center;justify-content:space-between;padding:0 32px}
.brand{font-family:"Raleway",Arial,sans-serif;font-weight:800;font-size:30px;color:var(--red);display:flex;align-items:center;gap:10px}
.brand-dot{width:14px;height:14px;border-radius:50%;background:var(--ink)}
.header-icons{display:flex;gap:10px}
.header-icons span{width:26px;height:26px;border-radius:50%;border:2px solid var(--line);background:var(--white)}
.main-nav{height:44px;background:var(--nav);display:flex;padding:0 32px}
.main-nav a{color:#d7d9dc;text-decoration:none;font-size:12px;font-weight:600;padding:0 18px;display:flex;align-items:center}
.main-nav a.active{background:var(--red);color:var(--white)}
.hero{position:relative;height:568px;background:linear-gradient(180deg,#9fb9cf 0%,#c7d5cf 22%,#7f9a58 40%,#6b8a43 70%,#56743a 100%)}
.hero-caption{position:absolute;right:40px;top:248px;width:540px;height:220px;background:rgba(18,18,20,.86);padding:30px 34px;color:var(--white)}
.hero-caption h1{font-family:"Raleway",Arial,sans-serif;font-weight:800;font-size:34px;line-height:1.12;text-align:right;letter-spacing:.5px}
.hero-caption p{font-size:11px;color:#c9cbce;text-align:right;margin-top:10px}
.hero-caption .btn{position:absolute;right:34px;bottom:22px;background:var(--white);color:var(--ink);font-size:11px;font-weight:700;padding:8px 16px}
.hero-arrows{position:absolute;left:50%;bottom:26px;transform:translateX(-50%);display:flex;gap:16px}
.hero-arrows svg{width:16px;height:22px}
.section-title{font-family:"Raleway",Arial,sans-serif;font-weight:800;font-size:22px;color:var(--ink);padding:28px 32px 0;height:88px}
.content{display:flex;gap:32px;padding:0 32px;height:1808px}
.auction-grid{width:748px;display:grid;grid-template-columns:1fr 1fr;grid-auto-rows:440px;gap:12px 16px}
.auction-card{background:var(--white);border:1px solid var(--line);padding:0 16px}
.auction-card h3{font-family:"Raleway",Arial,sans-serif;font-size:13px;font-weight:800;color:var(--ink);text-align:center;padding:14px 0 12px}
.auction-photo{height:176px}
.photo-a{background:linear-gradient(180deg,#8ea7bf,#a9a08a 55%,#6f7d4c)}
.photo-b{background:linear-gradient(180deg,#9fbbd6,#d9cdb4 50%,#7d8f56)}
.photo-c{background:linear-gradient(180deg,#b6cbe0,#e8e6e0 55%,#6e8f4a)}
.auction-card h4{font-family:"Raleway",Arial,sans-serif;color:var(--red);font-size:16px;font-weight:700;margin-top:14px}
.auction-card .desc{font-size:11px;margin-top:4px}
.meta{display:flex;gap:8px;margin-top:12px;font-size:11px}
.meta svg{width:16px;height:16px;flex:none;margin-top:1px}
.meta b{color:var(--ink);width:58px;flex:none}
.sidebar{width:356px;display:flex;flex-direction:column;gap:14px}
.widget{background:var(--white);border:1px solid var(--line)}
.widget-title{background:var(--ink);color:var(--white);font-family:"Raleway",Arial,sans-serif;font-weight:700;font-size:15px;padding:10px 14px}
.widget-body{padding:14px}
.signup input{display:block;width:100%;height:30px;border:1px solid var(--line);margin-top:10px;padding:0 8px;font-size:11px;color:var(--muted)}
.signup .btn{display:block;margin-top:10px;background:var(--red);color:var(--white);text-align:center;font-weight:700;font-size:11px;padding:8px}
.social{display:flex;justify-content:center;gap:14px}
.social span{width:40px;height:40px;background:var(--ink)}
.post{display:flex;gap:12px;padding:8px 0;border-bottom:1px solid var(--line);font-size:11px}
.post:last-of-type{border-bottom:none}
.date{width:48px;height:44px;background:var(--ink);color:var(--white);text-align:center;font-weight:700;font-size:11px;line-height:1.2;padding-top:6px;flex:none}
.avatar{width:48px;height:48px;background:linear-gradient(135deg,#c9b7a6,#8b7a6b);flex:none;border-radius:2px}
.avatar.small{width:34px;height:34px}
.post strong{display:block;color:var(--ink);font-size:12px}
.view-all{display:block;text-align:right;color:var(--red);font-size:10px;font-weight:700;margin-top:4px}
.thumbs{display:flex;gap:10px}
.thumbs div{flex:1;height:84px}
.logo-band{height:220px;background:var(--white);margin-top:36px;text-align:center;padding-top:28px}
.logo-band .brand{justify-content:center;font-size:28px}
.partners{display:flex;justify-content:center;gap:60px;margin-top:40px}
.partners span{width:120px;height:56px;background:#d9dbde}
.partners span:nth-child(2){border-radius:28px}
.site-footer{height:276px;background:var(--footer);color:#c9cbce;padding:44px 80px 0}
.contacts{display:flex;justify-content:space-between;font-size:17px;color:var(--white);font-weight:600}
.contacts div,.address{display:flex;align-items:center;gap:14px}
.contacts svg,.address svg{width:22px;height:22px}
.address{margin-top:30px;font-size:14px}
.copyright{margin-top:60px;border-top:1px solid #34363a;padding-top:18px;text-align:center;font-size:11px;color:#7d8186}
</style>
</head>
<body>
<header class="site-header">
  <div class="brand"><span class="brand-dot"></span>Harlow Auction</div>
  <div class="header-icons"><span></span><span></span><span></span></div>
</header>
<nav class="main-nav">
  <a class="active">Home</a><a>Auctions</a><a>Real Estate Listings</a><a>Services</a><a>Appraisals</a><a>The Bidding Hall</a><a>About Us</a><a>Contact Us</a>
</nav>
<section class="hero" role="img" aria-label="Aerial photo of farmland with a farmhouse and fields">
  <div class="hero-caption">
    <h1>LOREM IPSUM DOLOR<br>SIT AMET LOROLSD</h1>
    <p>Lorem ipsum dolor sit amet, consectetur adipiscing elit sed do eiusmod tempor incididunt ut labore et dolore magna aliqua. Ut enim ad minim veniam.</p>
    <span class="btn">READ MORE</span>
  </div>
  <div class="hero-arrows">
    <svg viewBox="0 0 16 22"><path d="M12 2 3 11l9 9" fill="none" stroke="#fff" stroke-width="3"/></svg>
    <svg viewBox="0 0 16 22"><path d="M4 2l9 9-9 9" fill="none" stroke="#fff" stroke-width="3"/></svg>
  </div>
</section>

<h2 class="section-title">FEATURED AUCTIONS</h2>

<div class="content">
  <main class="auction-grid">
    <article class="auction-card"><h3>SEALED BID REAL ESTATE AUCTION</h3><div class="auction-photo photo-a" role="img" aria-label="Aerial photo of a rural property"></div><h4>Sealed Bid Auction</h4><p class="desc">Lorem ipsum dolor sit amet, consectetur adipiscing elit, sed do eiusmod tempor incididunt ut labore et dolore magna aliqua.</p><div class="meta"><svg viewBox="0 0 16 16"><rect x="1" y="3" width="14" height="12" fill="none" stroke="#555" stroke-width="1.5"/><path d="M1 7h14M5 1v4M11 1v4" stroke="#555" stroke-width="1.5"/></svg><b>Begins:</b><span>Wednesday, August 12, 2015 at 6:00 PM CST</span></div><div class="meta"><svg viewBox="0 0 16 16"><path d="M8 15s5-5 5-9A5 5 0 0 0 3 6c0 4 5 9 5 9z" fill="#555"/><circle cx="8" cy="6" r="2" fill="#fff"/></svg><b>Location:</b><span>Dorian Harlow Auction &amp; Realty<br>2207 N. Birch Ave<br>Evansville, IN 47790</span></div></article>
    <article class="auction-card"><h3>SEALED BID REAL ESTATE AUCTION</h3><div class="auction-photo photo-b" role="img" aria-label="Photo of a large two-storey house"></div><h4>Sealed Bid Auction</h4><p class="desc">Lorem ipsum dolor sit amet, consectetur adipiscing elit, sed do eiusmod tempor incididunt ut labore et dolore magna aliqua.</p><div class="meta"><svg viewBox="0 0 16 16"><rect x="1" y="3" width="14" height="12" fill="none" stroke="#555" stroke-width="1.5"/><path d="M1 7h14M5 1v4M11 1v4" stroke="#555" stroke-width="1.5"/></svg><b>Begins:</b><span>Wednesday, August 12, 2015 at 6:00 PM CST</span></div><div class="meta"><svg viewBox="0 0 16 16"><path d="M8 15s5-5 5-9A5 5 0 0 0 3 6c0 4 5 9 5 9z" fill="#555"/><circle cx="8" cy="6" r="2" fill="#fff"/></svg><b>Location:</b><span>Dorian Harlow Auction &amp; Realty<br>2207 N. Birch Ave<br>Evansville, IN 47790</span></div></article>
    <article class="auction-card"><h3>SEALED BID REAL ESTATE AUCTION</h3><div class="auction-photo photo-c" role="img" aria-label="Photo of a white house with porch"></div><h4>Sealed Bid Auction</h4><p class="desc">Lorem ipsum dolor sit amet, consectetur adipiscing elit, sed do eiusmod tempor incididunt ut labore et dolore magna aliqua.</p><div class="meta"><svg viewBox="0 0 16 16"><rect x="1" y="3" width="14" height="12" fill="none" stroke="#555" stroke-width="1.5"/><path d="M1 7h14M5 1v4M11 1v4" stroke="#555" stroke-width="1.5"/></svg><b>Begins:</b><span>Wednesday, August 12, 2015 at 6:00 PM CST</span></div><div class="meta"><svg viewBox="0 0 16 16"><path d="M8 15s5-5 5-9A5 5 0 0 0 3 6c0 4 5 9 5 9z" fill="#555"/><circle cx="8" cy="6" r="2" fill="#fff"/></svg><b>Location:</b><span>Dorian Harlow Auction &amp; Realty<br>2207 N. Birch Ave<br>Evansville, IN 47790</span></div></article>
    <article class="auction-card"><h3>SEALED BID REAL ESTATE AUCTION</h3><div class="auction-photo photo-b" role="img" aria-label="Photo of a large family home at dusk"></div><h4>Sealed Bid Auction</h4><p class="desc">Lorem ipsum dolor sit amet, consectetur adipiscing elit, sed do eiusmod tempor incididunt ut labore et dolore magna aliqua.</p><div class="meta"><svg viewBox="0 0 16 16"><rect x="1" y="3" width="14" height="12" fill="none" stroke="#555" stroke-width="1.5"/><path d="M1 7h14M5 1v4M11 1v4" stroke="#555" stroke-width="1.5"/></svg><b>Begins:</b><span>Wednesday, August 12, 2015 at 6:00 PM CST</span></div><div class="meta"><svg viewBox="0 0 16 16"><path d="M8 15s5-5 5-9A5 5 0 0 0 3 6c0 4 5 9 5 9z" fill="#555"/><circle cx="8" cy="6" r="2" fill="#fff"/></svg><b>Location:</b><span>Dorian Harlow Auction &amp; Realty<br>2207 N. Birch Ave<br>Evansville, IN 47790</span></div></article>
    <article class="auction-card"><h3>SEALED BID REAL ESTATE AUCTION</h3><div class="auction-photo photo-c" role="img" aria-label="Photo of a suburban house with garage"></div><h4>Sealed Bid Auction</h4><p class="desc">Lorem ipsum dolor sit amet, consectetur adipiscing elit, sed do eiusmod tempor incididunt ut labore et dolore magna aliqua.</p><div class="meta"><svg viewBox="0 0 16 16"><rect x="1" y="3" width="14" height="12" fill="none" stroke="#555" stroke-width="1.5"/><path d="M1 7h14M5 1v4M11 1v4" stroke="#555" stroke-width="1.5"/></svg><b>Begins:</b><span>Wednesday, August 12, 2015 at 6:00 PM CST</span></div><div class="meta"><svg viewBox="0 0 16 16"><path d="M8 15s5-5 5-9A5 5 0 0 0 3 6c0 4 5 9 5 9z" fill="#555"/><circle cx="8" cy="6" r="2" fill="#fff"/></svg><b>Location:</b><span>Dorian Harlow Auction &amp; Realty<br>2207 N. Birch Ave<br>Evansville, IN 47790</span></div></article>
    <article class="auction-card"><h3>SEALED BID REAL ESTATE AUCTION</h3><div class="auction-photo photo-a" role="img" aria-label="Photo of a row of townhouses"></div><h4>Sealed Bid Auction</h4><p class="desc">Lorem ipsum dolor sit amet, consectetur adipiscing elit, sed do eiusmod tempor incididunt ut labore et dolore magna aliqua.</p><div class="meta"><svg viewBox="0 0 16 16"><rect x="1" y="3" width="14" height="12" fill="none" stroke="#555" stroke-width="1.5"/><path d="M1 7h14M5 1v4M11 1v4" stroke="#555" stroke-width="1.5"/></svg><b>Begins:</b><span>Wednesday, August 12, 2015 at 6:00 PM CST</span></div><div class="meta"><svg viewBox="0 0 16 16"><path d="M8 15s5-5 5-9A5 5 0 0 0 3 6c0 4 5 9 5 9z" fill="#555"/><circle cx="8" cy="6" r="2" fill="#fff"/></svg><b>Location:</b><span>Dorian Harlow Auction &amp; Realty<br>2207 N. Birch Ave<br>Evansville, IN 47790</span></div></article>
    <article class="auction-card"><h3>SEALED BID REAL ESTATE AUCTION</h3><div class="auction-photo photo-b" role="img" aria-label="Photo of a brick country house"></div><h4>Sealed Bid Auction</h4><p class="desc">Lorem ipsum dolor sit amet, consectetur adipiscing elit, sed do eiusmod tempor incididunt ut labore et dolore magna aliqua.</p><div class="meta"><svg viewBox="0 0 16 16"><rect x="1" y="3" width="14" height="12" fill="none" stroke="#555" stroke-width="1.5"/><path d="M1 7h14M5 1v4M11 1v4" stroke="#555" stroke-width="1.5"/></svg><b>Begins:</b><span>Wednesday, August 12, 2015 at 6:00 PM CST</span></div><div class="meta"><svg viewBox="0 0 16 16"><path d="M8 15s5-5 5-9A5 5 0 0 0 3 6c0 4 5 9 5 9z" fill="#555"/><circle cx="8" cy="6" r="2" fill="#fff"/></svg><b>Location:</b><span>Dorian Harlow Auction &amp; Realty<br>2207 N. Birch Ave<br>Evansville, IN 47790</span></div></article>
    <article class="auction-card"><h3>SEALED BID REAL ESTATE AUCTION</h3><div class="auction-photo photo-c" role="img" aria-label="Photo of a modern house at dusk"></div><h4>Sealed Bid Auction</h4><p class="desc">Lorem ipsum dolor sit amet, consectetur adipiscing elit, sed do eiusmod tempor incididunt ut labore et dolore magna aliqua.</p><div class="meta"><svg viewBox="0 0 16 16"><rect x="1" y="3" width="14" height="12" fill="none" stroke="#555" stroke-width="1.5"/><path d="M1 7h14M5 1v4M11 1v4" stroke="#555" stroke-width="1.5"/></svg><b>Begins:</b><span>Wednesday, August 12, 2015 at 6:00 PM CST</span></div><div class="meta"><svg viewBox="0 0 16 16"><path d="M8 15s5-5 5-9A5 5 0 0 0 3 6c0 4 5 9 5 9z" fill="#555"/><circle cx="8" cy="6" r="2" fill="#fff"/></svg><b>Location:</b><span>Dorian Harlow Auction &amp; Realty<br>2207 N. Birch Ave<br>Evansville, IN 47790</span></div></article>
  </main>

  <aside class="sidebar">
    <section class="widget signup"><h3 class="widget-title">Newsletter Sign Up</h3><div class="widget-body"><p>Lorem ipsum dolor sit amet, consectetur adipiscing elit sed do eiusmod tempor.</p><input value="Email address" readonly><span class="btn">SUBSCRIBE</span></div></section>
    <section class="widget"><h3 class="widget-title">Social Media</h3><div class="widget-body social"><span></span><span></span><span></span></div></section>
    <section class="widget"><h3 class="widget-title">News</h3><div class="widget-body">
      <div class="post"><div class="date">19<br>Aug</div><p><strong>Lorem ipsum dolor sit amet</strong>consectetur adipiscing elit sed do eiusmod tempor.</p></div>
      <div class="post"><div class="date">19<br>Aug</div><p><strong>Lorem ipsum dolor sit amet</strong>consectetur adipiscing elit sed do eiusmod tempor.</p></div>
      <div class="post"><div class="date">19<br>Aug</div><p><strong>Lorem ipsum dolor sit amet</strong>consectetur adipiscing elit sed do eiusmod tempor.</p></div>
      <span class="view-all">VIEW ALL</span></div></section>
    <section class="widget"><h3 class="widget-title">Events Blog</h3><div class="widget-body">
      <div class="post"><div class="avatar" role="img" aria-label="Portrait photo"></div><p><strong>Lorem ipsum dolor sit amet</strong>consectetur adipiscing elit sed do eiusmod tempor incididunt.</p></div>
      <div class="post"><div class="avatar" role="img" aria-label="Portrait photo"></div><p><strong>Lorem ipsum dolor sit amet</strong>consectetur adipiscing elit sed do eiusmod tempor incididunt.</p></div>
      <span class="view-all">VIEW ALL</span></div></section>
    <section class="widget"><h3 class="widget-title">Testimonials</h3><div class="widget-body">
      <div class="post"><div class="avatar small" role="img" aria-label="Client portrait"></div><p>Lorem ipsum dolor sit amet, consectetur adipiscing elit sed do eiusmod tempor. <strong>- John Smith</strong></p></div>
      <div class="post"><div class="avatar small" role="img" aria-label="Client portrait"></div><p>Lorem ipsum dolor sit amet, consectetur adipiscing elit sed do eiusmod tempor. <strong>- Jane Smith</strong></p></div>
      <span class="view-all">VIEW ALL</span></div></section>
    <section class="widget"><h3 class="widget-title">Featured Auctions</h3><div class="widget-body"><div class="thumbs"><div class="photo-a" role="img" aria-label="House photo"></div><div class="photo-c" role="img" aria-label="House photo"></div></div><span class="view-all">VIEW ALL</span></div></section>
    <section class="widget"><h3 class="widget-title">Featured Listings</h3><div class="widget-body"><div class="thumbs"><div class="photo-b" role="img" aria-label="House photo"></div><div class="photo-a" role="img" aria-label="House photo"></div></div><span class="view-all">VIEW ALL</span></div></section>
  </aside>
</div>

<section class="logo-band">
  <div class="brand"><span class="brand-dot"></span>Harlow Auction</div>
  <div class="partners"><span></span><span></span><span></span><span></span></div>
</section>

<footer class="site-footer">
  <div class="contacts">
    <div><svg viewBox="0 0 24 24"><path d="M6 2l4 4-2 3c1 3 4 6 7 7l3-2 4 4-3 4C10 22 2 14 2 5z" fill="#fff"/></svg>812.555.0143</div>
    <div><svg viewBox="0 0 24 24"><path d="M6 2l4 4-2 3c1 3 4 6 7 7l3-2 4 4-3 4C10 22 2 14 2 5z" fill="#fff"/></svg>877.555.0178</div>
    <div><svg viewBox="0 0 24 24"><rect x="2" y="5" width="20" height="14" fill="none" stroke="#fff" stroke-width="2"/><path d="M2 5l10 8 10-8" fill="none" stroke="#fff" stroke-width="2"/></svg>marcus@harlowbidhouse.example</div>
  </div>
  <div class="address"><svg viewBox="0 0 24 24"><path d="M12 23s8-8 8-14a8 8 0 0 0-16 0c0 6 8 14 8 14z" fill="#fff"/><circle cx="12" cy="9" r="3" fill="#1c1d20"/></svg>Dorian Harlow Auction-Realty, 3418 Thistle Lane, New Harmony, IN 47209</div>
  <p class="copyright">© 2015 Harlow Auction. All rights reserved.</p>
</footer>
</body>
</html>
```